Brindlewick Solutions - Website for a CRM IT Services Provider to Non-profits

We need a website design for our company that provides IT services to non-profits to enable them to manage their donors and philanthropy within their organization.

We would like to see a design that uses the colors in our logo and a funky take on how to uniquely present a topic as boring as IT. Examples of sites that we really like: tamsinvoke.com, www.corabellquist.com, mintgable.com

The final design should communicate that we are a professional, yet creative company that is fun to work with.

Target Market(s)

Non-profits who tend to be young, creative types that are low-tech

Industry/Entity Type

It Company

Requirements
Must have
• Must include tabs for Home, Contact Us, About, Projects, and Blog. The site must use the logo we have attached on all of the page, in one way or another (it can be small & in the corner).

The site has to work on all mobile browsers (iphone, ipad).
Nice to have
• It would be great if I could supply some HTML for the Contact page that would allow me to capture leads and put them directly into my CRM application. It's very easy to set up.
Should not have
• The design should not use old-style fonts and should not have a lot of dark colors. Keep it similar to our logo, clean and simple. We're not looking for a busy home page.

```html
<!DOCTYPE html>
<html lang="en">
<head>
<meta charset="utf-8">
<title>Brindlewick Solutions</title>
<link href="https://fonts.googleapis.com/css2?family=Delius&family=Arimo&display=swap" rel="stylesheet">
<style>
:root{
  --paper:#ececec;
  --teal:#2f8fa4;
  --teal-light:#46a8ba;
  --teal-deep:#23758a;
  --teal-ink:#2a8aa2;
  --ink:#3a3a3a;
  --white:#ffffff;
  --pale:#d3dde0;
  --pink:#f2c9c9;
  --mint:#a9dcc9;
}
*{box-sizing:border-box;margin:0;padding:0}
html,body{width:1084px;height:1200px;overflow:hidden;background:var(--paper)}
.canvas{position:relative;width:1084px;height:1200px;overflow:hidden;font-family:"Delius",cursive;color:var(--ink)}
.backdrop{position:absolute;left:0;top:0}
.abs{position:absolute}

.main-nav{left:512px;top:0;width:460px;height:34px;background:linear-gradient(#3aa0b6,var(--teal-deep));border-radius:0 0 16px 16px;display:flex;align-items:center;padding:0 12px}
.main-nav a{color:var(--white);text-decoration:none;font-size:14px;padding:0 20px;border-left:1px solid rgba(255,255,255,.3);line-height:20px}
.main-nav a:first-child{border-left:none;background:var(--teal-light);border-radius:10px;padding:2px 18px}

.brand{left:120px;top:10px;width:190px;text-align:center}
.brand-dot{width:114px;height:114px;border-radius:50%;background:var(--teal-ink);margin:0 auto 8px}
.brand-name{font-size:27px;line-height:28px;color:var(--teal-ink)}

.social{left:713px;top:79px;display:flex;gap:5px}
.social span{width:28px;height:28px;border-radius:50%;background:#c9c9c9}
.social span:first-child{background:#3c5a99}

.hero-title{left:101px;top:208px;font-size:24px;color:var(--teal-ink);letter-spacing:1px}
.hero-text{left:100px;top:244px;width:352px;font-size:16px;line-height:27px;text-align:justify;letter-spacing:.5px}
.quote-btn{left:90px;top:397px;width:213px;height:41px;border-radius:21px;background:linear-gradient(var(--teal-light),var(--teal-deep));border:2px solid var(--white);box-shadow:0 2px 4px rgba(0,0,0,.2);color:var(--white);font-size:21px;line-height:37px;padding-left:20px}
.quote-icon{position:absolute;right:16px;top:-9px;width:40px;height:40px;border-radius:50%;background:radial-gradient(#6ee0d8,#1a9f9a);border:2px solid var(--white)}

.tablet{left:578px;top:122px;width:398px;height:332px;border-radius:22px;background:linear-gradient(135deg,#2a2a2a,#0e0e0e);box-shadow:0 3px 8px rgba(0,0,0,.3)}
.tablet-screen{position:absolute;left:37px;top:33px;width:324px;height:266px;background:linear-gradient(#f7f7f7,#dfe6ea)}

.dots{left:475px;top:560px;display:flex;gap:7px}
.dots span{width:18px;height:18px;border-radius:50%;background:var(--white)}
.dots span:first-child{background:var(--teal);border:2px solid var(--white)}

.special-title{left:106px;top:647px;font-size:29px;color:var(--white);letter-spacing:1px}
.special-sub{left:106px;top:696px;font-size:17px;color:var(--white);letter-spacing:.5px}
.special-text{left:108px;top:728px;width:503px;font-size:13.5px;line-height:21.7px;color:#e8f4f6;text-align:justify;letter-spacing:.4px}
.read-btn{left:106px;top:842px;width:89px;height:23px;border-radius:12px;background:var(--teal-deep);color:var(--white);font-size:12.5px;line-height:23px;text-align:center;box-shadow:inset 0 1px 0 rgba(255,255,255,.25)}

.news{left:697px;top:641px;width:282px;height:265px;border-radius:8px;background:rgba(120,200,215,.35);border:1px solid rgba(255,255,255,.25);padding:12px 22px}
.news h2{font-weight:normal;font-size:27px;color:var(--white);margin-bottom:16px;letter-spacing:1px}
.news-item{font-family:"Arimo",sans-serif;font-size:11.5px;line-height:20px;color:var(--white);margin-bottom:20px}
.news-item .link{color:#9fe6f2}
.news-item .age{color:#a9dbe4}

.work-label{left:100px;top:934px;font-size:22px;color:var(--white);letter-spacing:1px}
.work-title{left:102px;top:958px;font-size:43px;color:var(--white);letter-spacing:2px}
.work-note{left:153px;top:1020px;font-size:13px;color:var(--white);letter-spacing:.5px}
.portfolio-btn{left:173px;top:1045px;width:136px;height:30px;border-radius:15px;background:var(--teal-light);color:#ffe9a8;font-size:17px;line-height:30px;text-align:center}

.thumb{top:960px;width:200px;height:160px;background:var(--white);padding:6px;box-shadow:0 2px 5px rgba(0,0,0,.25)}
.thumb div{width:100%;height:100%}
.thumb-one{left:334px}.thumb-one div{background:linear-gradient(#fafafa 12%,#b57bd9 12%,#9c6bc2 72%,#fafafa 72%)}
.thumb-two{left:550px}.thumb-two div{background:linear-gradient(#e9e9e9 14%,#c98a52 14%,#7e5a44 74%,#f2f2f2 74%)}
.thumb-three{left:768px}.thumb-three div{background:linear-gradient(#fbfbfb 10%,#8c3f86 10%,#b864a6 72%,#fbfbfb 72%)}

.divider{left:99px;top:1147px;width:887px;border-top:4px dashed #2c7f93}

.footer{left:0;top:1172px;width:1084px;height:28px;background:var(--teal-deep)}
.footer-nav{left:99px;top:1176px;font-size:13px;color:var(--white);letter-spacing:.5px}
.footer-nav a{color:var(--white);text-decoration:none}
.footer-nav .sep{margin:0 12px}
.copyright{right:96px;top:1176px;font-size:13px;color:var(--white);letter-spacing:.5px}
</style>
</head>
<body>
<div class="canvas">
  <svg class="backdrop" width="1084" height="1200" viewBox="0 0 1084 1200">
    <rect width="1084" height="1200" fill="var(--paper)"/>
    <circle cx="54" cy="415" r="100" fill="var(--pale)" opacity=".7"/>
    <circle cx="108" cy="505" r="24" fill="var(--pale)"/>
    <circle cx="540" cy="221" r="36" fill="var(--pink)" opacity=".8"/>
    <circle cx="406" cy="495" r="50" fill="#dde3e6"/>
    <circle cx="1084" cy="430" r="50" fill="#eed8d3"/>
    <circle cx="307" cy="515" r="25" fill="var(--mint)"/>
    <circle cx="332" cy="476" r="38" fill="#7ebfc8"/>
    <ellipse cx="742" cy="505" rx="140" ry="30" fill="#e1e1e1"/>
    <path d="M0 587 L210 587 C330 560 400 519 560 519 C720 519 800 560 920 587 L1084 587 L1084 1200 L0 1200 Z" fill="var(--teal)"/>
    <path d="M230 587 C420 640 700 640 900 587" fill="var(--teal-light)" opacity=".5"/>
    <circle cx="172" cy="668" r="81" fill="var(--teal-light)" opacity=".45"/>
    <circle cx="530" cy="790" r="40" fill="var(--teal-light)" opacity=".4"/>
    <circle cx="285" cy="1090" r="30" fill="var(--teal-light)" opacity=".45"/>
    <path d="M630 645 L665 745 L655 720 M665 745 L640 735" fill="none" stroke="#e6f4f7" stroke-width="6" stroke-dasharray="3 3" stroke-linecap="round"/>
    <path d="M170 1050 C115 1060 100 1010 122 990 M170 1050 L150 1034 M170 1050 L152 1066" fill="none" stroke="#5cc8e6" stroke-width="9" stroke-linecap="round"/>
  </svg>

  <nav class="abs main-nav">
    <a href="#">Home</a><a href="#">About</a><a href="#">Projects</a><a href="#">Blog</a><a href="#">Contact Us</a>
  </nav>

  <div class="abs brand">
    <div class="brand-dot"></div>
    <div class="brand-name">Brindlewick<br>Solutions</div>
  </div>

  <div class="abs social"><span></span><span></span><span></span><span></span><span></span><span></span><span></span></div>

  <h1 class="abs hero-title">Measure What Matters</h1>
  <p class="abs hero-text">We provide consulting services for the Cloudtrellis.com platform, including full life-cycle implementations, health checks, business process mapping, and ROI analysis.</p>
  <div class="abs quote-btn">Get A Quote<span class="quote-icon"></span></div>

  <div class="abs tablet"><div class="tablet-screen" role="img" aria-label="Tablet screen showing a sales executive dashboard with charts and tables"></div></div>

  <div class="abs dots"><span></span><span></span><span></span><span></span><span></span><span></span></div>

  <h2 class="abs special-title">What Makes Us Special</h2>
  <p class="abs special-sub">Web based services and training for businesses and individuals</p>
  <p class="abs special-text">Our consultants understand sales operations, for both traditional sales organizations and nonprofits. We can help you build processes to streamline your sales and fundraising cycles. Our analytics measure the success of these process so that you can fine tune them.</p>
  <div class="abs read-btn">Readmore</div>

  <section class="abs news">
    <h2>Latest News</h2>
    <p class="news-item">Woah, KVT actually made (very nearly) the right decision <span class="link">http://lnk.to/q7Rw2k</span><br>Looking forward to next weeks smorgasbord.<br><span class="age">3 days ago</span></p>
    <p class="news-item">Woah, KVT actually made (very nearly) the right decision <span class="link">http://lnk.to/q7Rw2k</span><br>Looking forward to next weeks smorgasbord.<br><span class="age">3 days ago</span></p>
  </section>

  <div class="abs work-label">Latest</div>
  <div class="abs work-title">Work</div>
  <div class="abs work-note">don't forget to check ou my</div>
  <div class="abs portfolio-btn">Full Portfolio</div>

  <div class="abs thumb thumb-one"><div role="img" aria-label="Portfolio site for an illustrator with a purple ink drawing"></div></div>
  <div class="abs thumb thumb-two"><div role="img" aria-label="Association website with a large portrait photo banner"></div></div>
  <div class="abs thumb thumb-three"><div role="img" aria-label="Therapy resources website with a purple hand-drawn illustration"></div></div>

  <div class="abs divider"></div>
  <div class="abs footer"></div>
  <div class="abs footer-nav"><a href="#">Home</a><span class="sep">|</span><a href="#">About</a><span class="sep">|</span><a href="#">Projects</a><span class="sep">|</span><a href="#">Blog</a><span class="sep">|</span><a href="#">Contact Us</a></div>
  <div class="abs copyright">Copyright © 2012 Brindlewick Solutions</div>
</div>
</body>
</html>
```